Rate sheet redesign

We provide rate sheets to agents for our scenic flights and I would like to make them easier to read and more comprehensive. I'd also like to be able to edit the information in the design, as tours get updated and so do the rates. We've got new product out of shark bay, so the sections would need to be: Perth, Geraldton, Kalbarri and Shark Bay. I've attached what we've been using and also some concept photos.

also a link to our flights online: https://ridgewaterairtours.tavlomo.com/catalog/418352/trips-from-perth

I've put this under brochure redesign as I wasn't sure what a rate sheet would be considered. Open to different formats if it means content is editable.

Need extra days to review

```html
<!DOCTYPE html>
<html lang="en">
<head>
<meta charset="utf-8">
<title>Geraldton Rates – Ridgewater Aviation</title>
<link rel="stylesheet" href="https://fonts.googleapis.com/css2?family=Poppins:wght@400;600;700;800&family=Roboto:wght@400;500;700&display=swap">
<style>
  :root {
    --brand-blue: #005a9c;
    --brand-orange: #ef9a27;
    --ink: #2b2b2b;
    --body-text: #555555;
    --note-text: #6a6a6a;
    --cell-bg: #f4f4f4;
    --panel-bg: #ffffff;
    --tab-bg: #e2e8ee;
    --page-bg-a: #eeeeee;
    --page-bg-b: #fafafa;
  }
  * { box-sizing: border-box; margin: 0; padding: 0; }
  html, body { width: 1200px; height: 927px; overflow: hidden; }
  body {
    position: relative;
    font-family: "Roboto", Arial, sans-serif;
    background: linear-gradient(135deg, var(--page-bg-a) 0%, var(--page-bg-b) 45%, var(--page-bg-a) 100%);
  }
  .brand {
    position: absolute; left: 96px; top: 58px;
    display: flex; align-items: center; gap: 10px;
  }
  .brand-dot { width: 30px; height: 30px; border-radius: 50%; background: var(--brand-blue); }
  .brand-name {
    font-weight: 500; font-size: 24px; color: var(--brand-blue); line-height: 1.1;
  }
  .region-tabs {
    position: absolute; left: 96px; top: 128px;
    display: flex; gap: 6px; list-style: none;
  }
  .region-tab {
    font-family: "Poppins", Arial, sans-serif; font-weight: 600;
    font-size: 11px; letter-spacing: 0.6px; text-transform: uppercase;
    padding: 5px 12px; border-radius: 3px;
    background: var(--tab-bg); color: var(--brand-blue);
  }
  .region-tab.is-current { background: var(--brand-orange); color: #fff; }
  .sheet-title {
    position: absolute; right: 90px; top: 30px;
    font-family: "Poppins", Arial, sans-serif; font-weight: 800;
    font-size: 45px; letter-spacing: 0.5px; color: var(--brand-blue);
  }
  .title-rule {
    position: absolute; left: 681px; top: 91px; width: 428px; height: 4px;
    background: var(--brand-orange);
  }
  .validity {
    position: absolute; right: 91px; top: 104px; text-align: right;
    font-family: "Poppins", Arial, sans-serif; font-weight: 700;
    font-size: 21px; line-height: 26px; color: var(--ink);
  }
  .rate-panel {
    position: absolute; left: 85px; top: 177px; width: 1029px; height: 654px;
    background: var(--panel-bg); padding: 5px 5px 6px 6px;
    box-shadow: 0 2px 14px rgba(0,0,0,0.12);
  }
  .rate-table {
    display: grid;
    grid-template-columns: 249px 249px 249px 126px 121px;
    grid-template-rows: 66px 189px 189px 187px;
    gap: 4px 6px;
  }
  .col-head {
    background: var(--brand-blue); color: #fff;
    font-weight: 700; font-size: 17.5px;
    display: flex; align-items: center; justify-content: center;
  }
  .flight-name {
    background: var(--brand-orange); color: #fff;
    font-weight: 500; font-size: 18px; line-height: 29px;
    display: flex; align-items: center; justify-content: center;
    text-align: center; padding: 0 14px;
  }
  .cell {
    background: var(--cell-bg); color: var(--body-text);
    font-size: 13px; line-height: 18.2px;
    display: flex; flex-direction: column; justify-content: center;
    padding: 0 18px 0 22px;
  }
  .included-label {
    color: var(--brand-orange); font-weight: 500; font-size: 15.5px; margin-bottom: 3px;
  }
  .cell p + p { margin-top: 18px; }
  .price {
    background: var(--cell-bg); color: var(--brand-orange);
    font-weight: 700; font-size: 15.5px;
    display: flex; align-items: center; justify-content: center;
  }
  .fee-note {
    position: absolute; left: 91px; top: 842px; width: 1000px;
    font-family: "Poppins", Arial, sans-serif; font-size: 13.6px; line-height: 18px;
    color: var(--note-text); text-transform: uppercase;
  }
  .page-code {
    position: absolute; left: 1160px; top: 898px;
    font-size: 10px; color: var(--note-text);
  }
</style>
</head>
<body>
  <div class="brand">
    <span class="brand-dot"></span>
    <span class="brand-name">Ridgewater<br>Aviation</span>
  </div>

  <ul class="region-tabs">
    <li class="region-tab">Perth</li>
    <li class="region-tab is-current">Geraldton</li>
    <li class="region-tab">Kalbarri</li>
    <li class="region-tab">Shark Bay</li>
  </ul>

  <h1 class="sheet-title">GERALDTON RATES</h1>
  <div class="title-rule"></div>
  <p class="validity">TOUR RATES VALID FROM 1ST APRIL 2025 TO<br>31ST MARCH 2026 – RETAIL RATES</p>

  <section class="rate-panel">
    <div class="rate-table">
      <div class="col-head">FLIGHT</div>
      <div class="col-head">INCLUSIONS</div>
      <div class="col-head">CLAUSES</div>
      <div class="col-head">ADULT</div>
      <div class="col-head">CHILD</div>

      <div class="flight-name">Abrolhos Island<br>Discovery Tour<br>(Flight 303)</div>
      <div class="cell">
        <span class="included-label">Included:</span>
        <p>Scenic flight from Geraldton to East Wallabi Island return. Morning /Afternoon Tea, and snorkel gear.</p>
        <p>Duration: 1 hour 20 minutes flight time 5 hours 30 minutes Total Tour time</p>
      </div>
      <div class="cell"><p>Normal departure time is 8am, however timing is flexible depending on bookings. Start time must be 6 hours before sunset.</p></div>
      <div class="price">$550.00</div>
      <div class="price">$385.00</div>

      <div class="flight-name">Abrolhos Island<br>Discovery Tour<br>plus Pink Lake (Flight 304)</div>
      <div class="cell">
        <span class="included-label">Included:</span>
        <p>Scenic flight from Geraldton to East Wallabi Island return via Pink Lake.</p>
        <p>Morning /Afternoon Tea, and snorkel gear. Duration: 2 hours flight time 6 hours Total Tour time</p>
      </div>
      <div class="cell"><p>Normal departure time is 8am, however timing is flexible depending on bookings. Start time must be 6 hours before sunset.</p></div>
      <div class="price">$610.00</div>
      <div class="price">$427.00</div>

      <div class="flight-name">Abrolhos Islands and<br>Batavia Shipwreck<br>(Flight 303B)</div>
      <div class="cell">
        <span class="included-label">Included:</span>
        <p>Scenic flight from Geraldton to East Wallabi Island return, and Morning /Afternoon Tea.</p>
        <p>Duration: 1 hour 20 minutes flight time 2 hours Total Tour time</p>
      </div>
      <div class="cell"><p>Normal departure time is 2pm, however timing is flexible depending on bookings. Start time must be 2.5 hours before sunset.</p></div>
      <div class="price">$500.00</div>
      <div class="price">$350.00</div>
    </div>
  </section>

  <p class="fee-note">Please note there is a new $11 government fee for all flights landing at the Abrolhos Islands, this is not a commissionable fee and needs to be paid on top of the nett rate</p>
  <span class="page-code">C38</span>
</body>
</html>
```